Insurance company needs a business card design

We need a business card design for a Massachusetts-based insurance company Cielora Insurance, LLC. We provide auto insurance to Hispanic (Spanish- or Portuguese-speaking) immigrants in the United States. We will give these business cards to auto dealers where such customers typically go to purchase vehicles. We will provide a solution to the dealers to provide easy insurance to the customers buying cars at their dealerships. Cielora is the Spanish word for protection.
Contact Information for Business Card
Name, Designation, Company Name, Address, Phone Number, Email, Website
Look and feel
Each slider illustrates characteristics of the customer's brand and the style your logo design should communicate.

```html
<!DOCTYPE html>
<html lang="en">
<head>
<meta charset="utf-8">
<title>Cielora Insurance – Business Card</title>
<link rel="stylesheet" href="https://fonts.googleapis.com/css2?family=Montserrat:wght@400;500;700;800&display=swap">
<style>
  :root {
    --backdrop: #1a1a1a;
    --card: #2a2a2a;
    --card-edge: #232323;
    --orange: #f08a0c;
    --blue: #0f5a94;
    --white: #f2f2f2;
  }
  * { box-sizing: border-box; margin: 0; padding: 0; }
  html, body {
    width: 1200px; height: 900px; overflow: hidden;
    background: var(--backdrop);
    font-family: "Montserrat", sans-serif;
  }
  .stage {
    width: 1200px; height: 900px;
    display: flex; flex-direction: column; align-items: center; justify-content: center;
    gap: 40px;
  }
  .card {
    position: relative;
    width: 700px; height: 400px;
    background: linear-gradient(135deg, var(--card) 0%, var(--card-edge) 100%);
    border-bottom: 5px solid var(--orange);
    box-shadow: 0 10px 30px rgba(0,0,0,.5);
  }
  /* brand lockup */
  .brand { display: flex; align-items: center; gap: 16px; }
  .brand-mark {
    width: 58px; height: 58px; background: var(--orange); flex: none;
  }
  .brand-name {
    color: var(--blue); font-weight: 800; line-height: 1;
    text-transform: uppercase; letter-spacing: 1px;
  }
  .brand-name .sub { display: block; font-size: .42em; letter-spacing: 8px; margin-top: 6px; }

  .card-front { display: flex; align-items: center; justify-content: center; }
  .card-front .brand-name { font-size: 52px; }

  .card-back { display: flex; align-items: center; padding: 0 50px 0 50px; }
  .card-back .brand { flex-direction: column; gap: 14px; width: 280px; text-align: center; }
  .card-back .brand-mark { width: 80px; height: 80px; }
  .card-back .brand-name { font-size: 46px; }
  .divider { width: 2px; height: 190px; background: var(--orange); margin: 0 38px 0 20px; flex: none; }

  .contact { color: var(--white); font-size: 17px; line-height: 1.45; }
  .contact .person { color: var(--orange); font-weight: 800; font-size: 30px; text-transform: uppercase; line-height: 1.1; }
  .contact .role { text-transform: uppercase; font-size: 15px; margin-bottom: 14px; letter-spacing: 1px; }
  .contact .address { margin-bottom: 8px; }
  .contact-line { display: flex; align-items: center; gap: 8px; }
  .contact-line svg { width: 14px; height: 14px; flex: none; }
</style>
</head>
<body>
<main class="stage">
  <section class="card card-front" aria-label="Card front">
    <div class="brand">
      <span class="brand-mark"></span>
      <span class="brand-name">Cielora<span class="sub">Insurance</span></span>
    </div>
  </section>

  <section class="card card-back" aria-label="Card back">
    <div class="brand">
      <span class="brand-mark"></span>
      <span class="brand-name">Cielora<span class="sub">Insurance</span></span>
    </div>
    <span class="divider"></span>
    <div class="contact">
      <p class="person">Daniel Reyes</p>
      <p class="role">President</p>
      <p class="address">2218 Harbor Lane<br>Lowell, MA 01852</p>
      <p class="contact-line">
        <svg viewBox="0 0 16 16" fill="none" stroke="#f08a0c" stroke-width="1.6"><path d="M4 2l2.5 3-1.5 1.5c.8 1.8 2.2 3.2 4 4L10.5 9l3 2.5-1.5 2C7 13 3 9 2.5 4z"/></svg>
        617-555-0148
      </p>
      <p class="contact-line">
        <svg viewBox="0 0 16 16" fill="none" stroke="#f08a0c" stroke-width="1.4"><rect x="1.5" y="3.5" width="13" height="9"/><path d="M1.5 3.5l6.5 5 6.5-5"/></svg>
        info@cielorainsurance.com
      </p>
      <p class="contact-line">
        <svg viewBox="0 0 16 16" fill="none" stroke="#f08a0c" stroke-width="1.3"><circle cx="8" cy="8" r="6.5"/><path d="M1.5 8h13M8 1.5c3 3.5 3 9.5 0 13M8 1.5c-3 3.5-3 9.5 0 13"/></svg>
        www.cielorainsurance.com
      </p>
    </div>
  </section>
</main>
</body>
</html>
```